Hochzeits-Einladungen
Zielgruppe
Damen im Alter zwischen 25 - 40 Jahren, die gerade ihr Hochzeit planen
Aufgabenstellung
Gestaltung von Hochzeitskarten-Enladungen
Formate (in mm):
- geschlossen 145x145 (offen290x145)
ODER
- geschlossen 210x100 (offen420x100)
Vorgaben Design:
Es können auch Fotos des Paares als Design-Bestandteil eingebaut werden. Ein Foto oder mehrere (für diese Fotos einfach irgendwelche Paltzhalter verwenden – keine Fotos erwerben!)
Keine Verwendung von Sonderfarben (Digitaldruck ->CMYK) wie z.B. Gold, Silber etc..
Verwendung nur von Commercial-Use-Free-Fonts (Bitte hiervon auswählen: www.glyphmarmot.com)
Zur Abnahme:
Zuerst die Design-Entwürfe als PDF
Dann als InDesign (alles in unterschiedlichen Layern angelegt, die Illustrationen etc. als Vector und in CMYK)
klassisch - schlicht - mit hochzeitstypischen Illustrationen

```html
<!DOCTYPE html>
<html lang="de">
<head>
<meta charset="utf-8">
<title>Hochzeitseinladung – Jonas &amp; Liesel</title>
<link rel="stylesheet" href="https://fonts.googleapis.com/css2?family=EB+Garamond:ital,wght@0,400;1,600&family=Great+Vibes&family=Parisienne&display=swap">
<style>
  :root {
    --paper: #ffffff;
    --backdrop: #ffffff;
    --frame: #a3a3a3;
    --shadow: #c4c4c4;
    --ink: #4a4a4a;
    --ink-soft: #6e6e6e;
    --leaf: #3f9a3c;
    --meadow: #c3dfa5;
  }
  * { margin: 0; padding: 0; box-sizing: border-box; }
  html, body {
    width: 1126px; height: 1200px; overflow: hidden;
    background: var(--backdrop);
  }
  .canvas { position: relative; width: 1126px; height: 1200px; }

  .spread {
    position: absolute; left: 86px; width: 944px; height: 473px;
    background: var(--paper);
    border: 1.5px solid var(--frame);
    box-shadow: 6px 6px 0 var(--shadow);
    overflow: hidden;
  }
  .spread--outside { top: 68px; }
  .spread--inside { top: 654px; }

  .script-heading {
    position: absolute;
    font-family: "Parisienne", cursive;
    font-size: 17px; color: var(--ink);
    text-align: center; white-space: nowrap;
    transform: translateX(-50%);
  }
  .body-copy {
    position: absolute;
    font-family: "EB Garamond", serif;
    font-size: 11px; line-height: 15px; color: var(--ink-soft);
    text-align: center;
    transform: translateX(-50%);
  }
  .body-copy p + p { margin-top: 15px; }
  .body-copy em { font-style: italic; font-weight: 600; color: var(--ink); }

  .portrait { position: absolute; width: 84px; height: 113px; }
  .portrait__mat {
    position: absolute; inset: -4px -6px -6px -4px;
    background: var(--leaf);
  }
  .portrait__photo { position: absolute; inset: 0; }
  .portrait--groom .portrait__mat { transform: rotate(-11deg); }
  .portrait--groom .portrait__photo { background: linear-gradient(160deg, #3d6a3a 0%, #b9bcb6 45%, #d9dad6 100%); }
  .portrait--bride .portrait__mat { transform: rotate(9deg); }
  .portrait--bride .portrait__photo { background: linear-gradient(170deg, #496f3f 0%, #d6b69a 45%, #f1ece6 100%); }

  .couple-names {
    position: absolute; left: 708px; top: 78px; transform: translateX(-50%);
    font-family: "Great Vibes", cursive; color: var(--ink-soft);
    text-align: center; font-size: 30px; line-height: 36px;
  }
  .couple-names__tagline {
    display: block; margin-top: 22px;
    font-family: "Parisienne", cursive; font-size: 19px;
  }

  .hearts-art {
    position: absolute; left: 756px; top: 333px; width: 154px; height: 104px;
    border-radius: 45% 45% 40% 40%;
    background: radial-gradient(ellipse at 50% 45%, #8fc77a 0%, #d5ebc6 60%, rgba(255,255,255,0) 75%);
  }

  .meadow { position: absolute; left: 0; bottom: 0; width: 944px; height: 30px; }
</style>
</head>
<body>
<main class="canvas">

  <section class="spread spread--outside" aria-label="Außenseite der Einladung">
    <h2 class="script-heading" style="left:231px; top:110px;">Lorem ipsum dolor sit amet,&nbsp; consectetuer adipiscing elit.</h2>
    <div class="body-copy" style="left:231px; top:156px; width:275px;">
      <p>Nulla consequat massa quis enim. Donec pede justo, fringilla vel, aliquet nec, vulputate eget, arcu. In enim justo, rhoncus ut, imperdiet a, venenatis vitae, justo.</p>
    </div>

    <figure class="portrait portrait--groom" style="left:505px; top:99px;">
      <div class="portrait__mat"></div>
      <div class="portrait__photo" role="img" aria-label="Foto des Bräutigams im hellen Anzug"></div>
    </figure>

    <h1 class="couple-names">Jonas<br>&amp;<br>Liesel
      <span class="couple-names__tagline">trauen sich</span>
    </h1>

    <figure class="portrait portrait--bride" style="left:827px; top:99px;">
      <div class="portrait__mat"></div>
      <div class="portrait__photo" role="img" aria-label="Foto der Braut im Brautkleid"></div>
    </figure>

    <div class="hearts-art" role="img" aria-label="Gemalte Illustration zweier verschlungener grüner Herzen"></div>

    <svg class="meadow" viewBox="0 0 944 30" preserveAspectRatio="none" aria-hidden="true">
      <path fill="var(--meadow)" d="M0 18 C60 14 120 16 180 13 C230 11 260 16 320 15 C380 14 410 12 440 11 C470 10 500 13 540 9 C580 6 620 12 680 10 C720 9 760 13 800 12 C840 11 880 14 944 16 L944 30 L0 30 Z"/>
    </svg>
  </section>

  <section class="spread spread--inside" aria-label="Innenseite der Einladung">
    <h2 class="script-heading" style="left:220px; top:74px;">Lorem ipsum dolor sit amet,&nbsp; consectetuer adipiscing elit.</h2>
    <div class="body-copy" style="left:220px; top:118px; width:260px;">
      <p><em>Lorem:</em> ipsum dolor sit amet<br><em>consectetuer:</em> adipiscing elit</p>
      <p><em>Aenean:</em> commodo ligula eget<br><em>dolor:</em> Aenean massa<br><em>Cum sociis:</em> natoque</p>
    </div>

    <h2 class="script-heading" style="left:706px; top:74px;">Lorem ipsum dolor sit amet,&nbsp; consectetuer adipiscing elit.</h2>
    <div class="body-copy" style="left:706px; top:118px; width:366px;">
      <p>Lorem ipsum dolor sit amet, consectetuer adipiscing elit. Aenean commodo ligula eget dolor. Aenean massa. Cum sociis natoque penatibus et magnis dis parturient montes, nascetur ridiculus mus. Donec quam felis, ultricies nec, pellentesque eu, pretium quis, sem.</p>
      <p>Nulla consequat massa quis enim. Donec pede justo, fringilla vel, aliquet nec, vulputate eget, arcu. In enim justo, rhoncus ut, imperdiet a, venenatis vitae, justo.</p>
      <p>Nullam dictum felis eu pede mollis pretium. Integer tincidunt. Cras dapibus. Vivamus elementum semper nisi.<br>Aliquam lorem ante, dapibus in, viverra quis, feugiat a, tellus. Phasellus viverra nulla ut metus varius laoreet. Quisque rutrum. Aenean imperdiet</p>
    </div>

    <svg class="meadow" viewBox="0 0 944 30" preserveAspectRatio="none" aria-hidden="true">
      <path fill="var(--meadow)" d="M0 18 C60 14 120 16 180 13 C230 11 260 16 320 15 C380 14 410 12 440 11 C470 10 500 13 540 9 C580 6 620 12 680 10 C720 9 760 13 800 12 C840 11 880 14 944 16 L944 30 L0 30 Z"/>
    </svg>
  </section>

</main>
</body>
</html>
```